Gourmet Chocolate Chip cookie company e-commerce website design

We would like to create a landing page for an e-commerce site for a gourmet chocolate chip cookie business. We are in the process of finalizing the "About Us" story.... A chic, clean, fresh, (don't forget yummy) site for "Tilly's Biscuits". Offers a "Cookies like Mom makes" for anyone who is missing home. Our cookies are homemade, artisan, small batch product. This will be a direct to consumer site for care packages, gifts, occasions as well as business and corporate events. For the landing page, we would like customers to be able to place an order and or inquire further about our product as well as links to social media (Instagram, Facebook and Linkedin and email). We would like to transition by end of year to a full Shopify platform, for customers and consumers to process and ship all orders. We do not have official photography yet, but we have included some sneak peaks from inside the kitchen. A couple of key phrases that describe our brand: "If you love cookie dough, you will love these cookies" "It tastes as good as it looks" "Its pure love and happiness" "Puts a smile on your face" "Tastes like home" These cookies have been in the family for 40+ years and its time to share! Our goal is to make this a lifestyle brand.
https://www.vrx.example/2018/08/30/health/chocolate-chip-cookies-addictive-food-lomax/index.html
a tester shopify page:
https://qtrm5k8dplzn3vay-5817264081.storepeekdemo.example/
Target Market(s)
direct to consumer focusing on 'the gift giver', being that this is a gourmet product, the sell price falls under the 'luxury category'. Goal is to target occasions, college kids, corporate and business events
Number of Pages Required
4 page
Font styles to use
Other font styles liked:
- see branding and logos attached
Requirements
Must have
- Initially, a landing page is a necessity and then a full workable website on the Shopify platform.
- Full website will include, shop, about us, gallery (linked to instagram), press, cart, terms and conditions. (access to all social media accounts)
Nice to have
- Inspo brands we love:
- Meadowlane Petals
- Dorian Vale
- Pemberly Hart
- Crumbles
Should not have
- SHOULD NOT LOOK LIKE MRS HADLEY
- Please call or email with questions

```html
<!DOCTYPE html>
<html lang="en">
<head>
<meta charset="utf-8">
<title>Tilly's Biscuits — Homemade Gourmet Cookies</title>
<link href="https://fonts.googleapis.com/css2?family=Great+Vibes&family=Lato:wght@300;400;700&family=Playfair+Display:wght@400;700&display=swap" rel="stylesheet">
<style>
:root{
  --peach:#fbe3c2;
  --peach-light:#fdf0dc;
  --peach-deep:#f3d2a3;
  --cream:#fffaf2;
  --white:#ffffff;
  --brown:#5a3a22;
  --brown-dark:#2a1a10;
  --brown-footer:#21150c;
  --caramel:#b07a45;
  --text:#6b5643;
  --muted:#9b8874;
  --line:#e8d9c6;
  --accent:#c8955a;
}
*{box-sizing:border-box;margin:0;padding:0}
html,body{width:670px;height:1200px;overflow:hidden}
body{font-family:'Lato',Arial,sans-serif;color:var(--text);background:var(--white);position:relative}
.script{font-family:'Great Vibes',cursive;font-weight:400}

/* hero */
.hero{position:absolute;left:0;top:0;width:670px;height:263px;background:linear-gradient(180deg,var(--peach) 0%,var(--peach-light) 100%)}
.site-header{position:absolute;left:123px;top:18px;width:424px;height:30px;background:var(--white);display:flex;align-items:center;justify-content:space-between;padding:0 10px;box-shadow:0 1px 3px rgba(120,80,40,.15)}
.brand{font-family:'Playfair Display',serif;font-size:12px;color:var(--brown);font-weight:400;display:flex;align-items:center;gap:5px}
.brand-dot{width:7px;height:7px;border-radius:50%;background:var(--caramel)}
.main-nav{display:flex;align-items:center;gap:9px;font-size:5.5px;letter-spacing:.5px;color:var(--muted)}
.main-nav a{color:inherit;text-decoration:none}
.main-nav .phone{display:flex;align-items:center;gap:3px;color:var(--caramel);margin-left:4px}
.hero-photo{position:absolute;left:223px;top:70px;width:212px;height:120px;border-radius:50% 50% 40% 40%/60% 60% 40% 40%;background:radial-gradient(ellipse at 55% 45%,#c98a4b 0%,#a86a35 45%,#e9c69a 78%,rgba(251,227,194,0) 100%)}
.ingredients{position:absolute;left:434px;top:98px;font-size:5px;line-height:8px;color:var(--caramel)}
.ingredients strong{display:block;font-family:'Playfair Display',serif;font-size:7px;color:var(--brown);margin-bottom:2px}
.arrow{position:absolute;top:126px;width:12px;height:20px}
.arrow.prev{left:121px}.arrow.next{left:535px}
.welcome{position:absolute;left:0;top:190px;width:670px;text-align:center;font-size:25px;color:var(--brown)}
.hero-copy{position:absolute;left:0;top:222px;width:670px;text-align:center;font-size:6px;line-height:9px;color:var(--muted);font-style:italic}

/* features */
.features{position:absolute;left:0;top:263px;width:670px;height:280px;background:var(--white)}
.flowers{position:absolute;right:0;top:0;width:220px;height:170px;background:radial-gradient(ellipse at 70% 45%,rgba(235,170,175,.55) 0%,rgba(245,215,210,.35) 40%,rgba(255,255,255,0) 75%)}
.promo{position:absolute;top:17px;height:96px;overflow:hidden}
.promo.baked{left:127px;width:203px;background:linear-gradient(90deg,#3a2618 0%,#1c120b 100%)}
.promo.gifts{left:335px;width:212px;background:linear-gradient(90deg,#7d6a5c 0%,#4a3d33 100%)}
.promo-photo{position:absolute;left:0;top:0;width:90px;height:96px;background:radial-gradient(ellipse at 50% 50%,#8a5a32 0%,#4a2e19 70%,rgba(28,18,11,0) 100%)}
.promo.gifts .promo-photo{width:130px;background:radial-gradient(ellipse at 50% 55%,#c9b9a8 0%,#8c7a6a 55%,rgba(74,61,51,0) 100%)}
.promo-text{position:absolute;right:12px;top:22px;text-align:center;color:var(--white)}
.promo-text .script{font-size:17px;display:block;color:#f4dcb8}
.promo-text small{display:block;font-size:5px;letter-spacing:.5px;margin:2px 0 6px;color:#e8d6c0}
.btn{display:inline-block;background:var(--accent);color:var(--white);font-size:5px;letter-spacing:.8px;padding:3px 8px;text-decoration:none}
.promo.gifts .promo-text{top:52px}
.section-title{font-size:15px;color:var(--brown)}
.choice-title{position:absolute;left:127px;top:128px}
.choice-list{position:absolute;left:123px;top:158px;width:424px;display:flex;justify-content:space-between}
.choice-item{width:54px;text-align:center}
.choice-photo{width:46px;height:36px;margin:0 auto 5px;border-radius:50%;background:radial-gradient(circle,#c48a52 0%,#a06a38 60%,#f3e6d6 100%)}
.choice-item:nth-child(3) .choice-photo{border-radius:3px;background:linear-gradient(135deg,#e6c28d,#c99a5e)}
.choice-item:nth-child(4) .choice-photo{background:radial-gradient(circle,#7a4a2a 0%,#5a331c 60%,#f3e6d6 100%)}
.choice-item:nth-child(6) .choice-photo{background:radial-gradient(circle,#e8c9a2 0%,#d2a775 60%,#f7ede0 100%)}
.choice-name{font-size:4.5px;color:var(--muted);line-height:6px}
.choice-price{font-size:5px;color:var(--caramel);margin-top:1px}
.slider{position:absolute;left:185px;top:258px;width:300px;height:1px;background:var(--line)}
.slider span{position:absolute;left:130px;top:-1px;width:40px;height:3px;background:var(--muted)}

/* about */
.about{position:absolute;left:0;top:543px;width:670px;height:197px;background:linear-gradient(180deg,var(--peach-deep) 0%,var(--peach) 100%)}
.about-title{position:absolute;left:127px;top:12px}
.about-copy{position:absolute;left:127px;top:42px;width:198px;font-size:5.5px;line-height:9px;color:var(--brown)}
.about-copy p+p{margin-top:5px}
.about .btn{position:absolute;left:127px;top:142px;background:var(--brown);padding:4px 10px}
.gallery{position:absolute;left:335px;top:12px;width:212px;height:170px}
.gallery div{position:absolute}
.g1{left:110px;top:0;width:50px;height:42px;background:linear-gradient(135deg,#f1e6d5,#cdb89c)}
.g2{left:164px;top:0;width:48px;height:42px;background:linear-gradient(135deg,#3a3a3a,#d9d9d9)}
.g3{left:0;top:46px;width:90px;height:80px;background:linear-gradient(135deg,#e9dccb,#b9a58b)}
.g4{left:94px;top:46px;width:118px;height:124px;background:radial-gradient(ellipse at 50% 55%,#d5a368 0%,#b07a45 50%,#8a8680 100%)}

/* best sellers */
.best{position:absolute;left:0;top:740px;width:670px;height:270px;background:var(--white)}
.best-title{position:absolute;left:0;top:12px;width:670px;text-align:center}
.best-grid{position:absolute;left:127px;top:40px;width:420px;display:grid;grid-template-columns:repeat(4,96px);column-gap:12px;row-gap:16px}
.product{text-align:center}
.product-photo{height:66px;background:linear-gradient(135deg,#dfc29a,#b98850)}
.product:nth-child(2) .product-photo{background:linear-gradient(135deg,#e8d8c2,#a77d52)}
.product:nth-child(3) .product-photo{background:linear-gradient(135deg,#f2e4cf,#c9a77c)}
.product:nth-child(4) .product-photo{background:linear-gradient(135deg,#eaf1f4,#d6b98b)}
.product:nth-child(5) .product-photo{background:linear-gradient(135deg,#8fb4d8,#e9b86d)}
.product:nth-child(6) .product-photo{background:linear-gradient(135deg,#6b8a3e,#c99a5e)}
.product:nth-child(7) .product-photo{background:linear-gradient(135deg,#f5ead8,#d9b88c)}
.product:nth-child(8) .product-photo{background:linear-gradient(135deg,#f0d49c,#c38a3e)}
.product-name{font-size:6px;color:var(--brown);margin-top:5px}
.product-price{font-size:6px;color:var(--caramel);margin-top:3px}

/* footer */
.site-footer{position:absolute;left:0;top:1010px;width:670px;height:190px;background:linear-gradient(180deg,var(--brown-dark),var(--brown-footer));color:#cdb9a3}
.footer-col{position:absolute;top:20px}
.footer-col h4{font-size:6px;letter-spacing:1px;color:var(--white);font-weight:700;margin-bottom:10px}
.contact{left:127px;width:160px}
.contact li{list-style:none;display:flex;align-items:center;gap:6px;font-size:5px;margin-bottom:8px}
.newsletter{left:300px;width:140px}
.subscribe{display:flex;height:12px}
.subscribe span{flex:1;background:var(--white)}
.subscribe b{background:var(--accent);color:var(--white);font-size:5px;padding:0 7px;display:flex;align-items:center;letter-spacing:.5px}
.quick{left:458px;width:90px}
.quick li{list-style:none;font-size:5px;margin-bottom:5px}
.footer-bar{position:absolute;left:127px;top:160px;width:420px;border-top:1px solid rgba(255,255,255,.12);padding-top:8px;display:flex;justify-content:space-between;align-items:center;font-size:5px;color:#9b8874}
.follow{display:flex;align-items:center;gap:5px}
.follow i{display:block;width:6px;height:6px;border-radius:50%;background:#9b8874}
</style>
</head>
<body>

<section class="hero">
  <header class="site-header">
    <div class="brand"><span class="brand-dot"></span>Tilly's Biscuits</div>
    <nav class="main-nav">
      <a>HOME</a><a>ABOUT US</a><a>PRODUCTS</a><a>MENU</a><a>CONTACT US</a>
      <span class="phone"><svg width="6" height="6" viewBox="0 0 10 10"><path d="M2 1l2 2-1 1.5c.7 1.3 1.5 2.1 2.5 2.5L7 6l2 2-1.5 1.5C4.5 9 1 5.5.5 2.5z" fill="currentColor"/></svg>(555) 014-2280</span>
    </nav>
  </header>
  <svg class="arrow prev" viewBox="0 0 12 20"><path d="M10 2L2 10l8 8" fill="none" stroke="#9b8874" stroke-width="2"/></svg>
  <svg class="arrow next" viewBox="0 0 12 20"><path d="M2 2l8 8-8 8" fill="none" stroke="#9b8874" stroke-width="2"/></svg>
  <div class="hero-photo" role="img" aria-label="Stack of chocolate chip cookies"></div>
  <div class="ingredients"><strong>Ingredients</strong>Butter<br>Sugar<br>Flour<br>Chocolate<br>Vanilla<br>Eggs<br>Love</div>
  <h1 class="welcome script">Welcome to Tilly's Biscuits</h1>
  <p class="hero-copy">"If you love cookie dough, you will love these cookies" "It tastes as good as it looks"<br>"It's pure love and happiness" "Puts a smile on your face" "Tastes like home"</p>
</section>

<section class="features">
  <div class="flowers" role="img" aria-label="Soft pink flowers in the background"></div>
  <div class="promo baked">
    <div class="promo-photo" role="img" aria-label="Stacked fresh baked cookies"></div>
    <div class="promo-text"><span class="script">Fresh Baked</span><small>GOURMET CHOCOLATE COOKIES</small><a class="btn">SHOP NOW</a></div>
  </div>
  <div class="promo gifts">
    <div class="promo-photo" role="img" aria-label="Wrapped cookie gift boxes"></div>
    <div class="promo-text"><a class="btn">ORDER NOW</a></div>
  </div>
  <h2 class="section-title script choice-title">Today's Choice</h2>
  <div class="choice-list">
    <div class="choice-item"><div class="choice-photo" role="img" aria-label="Chocolate chip cookie"></div><div class="choice-name">Classic Chip</div><div class="choice-price">$ 18.00</div></div>
    <div class="choice-item"><div class="choice-photo" role="img" aria-label="Chocolate chip cookie"></div><div class="choice-name">Double Chip</div><div class="choice-price">$ 20.00</div></div>
    <div class="choice-item"><div class="choice-photo" role="img" aria-label="Square shortbread biscuits"></div><div class="choice-name">Shortbread</div><div class="choice-price">$ 16.00</div></div>
    <div class="choice-item"><div class="choice-photo" role="img" aria-label="Dark chocolate cookie"></div><div class="choice-name">Dark Cocoa</div><div class="choice-price">$ 22.00</div></div>
    <div class="choice-item"><div class="choice-photo" role="img" aria-label="Chocolate chip cookie"></div><div class="choice-name">Sea Salt Chip</div><div class="choice-price">$ 20.00</div></div>
    <div class="choice-item"><div class="choice-photo" role="img" aria-label="Sugar cookie"></div><div class="choice-name">Sugar Cookie</div><div class="choice-price">$ 16.00</div></div>
    <div class="choice-item"><div class="choice-photo" role="img" aria-label="Chocolate chip cookie"></div><div class="choice-name">Oat Chip</div><div class="choice-price">$ 18.00</div></div>
  </div>
  <div class="slider"><span></span></div>
</section>

<section class="about">
  <h2 class="section-title script about-title">About Tilly's Biscuits</h2>
  <div class="about-copy">
    <p>These cookies have been in our family for over forty years, baked in small batches from a recipe passed down at the kitchen table. Every biscuit is homemade and artisan, just like Mom makes.</p>
    <p>Now it's time to share. Send a care package, a gift for an occasion or a treat for your next event, and bring a taste of home to anyone who is missing it.</p>
  </div>
  <a class="btn">READ MORE</a>
  <div class="gallery">
    <div class="g1" role="img" aria-label="Kitchen with baking ingredients"></div>
    <div class="g2" role="img" aria-label="Checked kettle on the stove"></div>
    <div class="g3" role="img" aria-label="Cookies cooling in the kitchen"></div>
    <div class="g4" role="img" aria-label="Tray of freshly baked cookies"></div>
  </div>
</section>

<section class="best">
  <h2 class="section-title script best-title">Best Sellers</h2>
  <div class="best-grid">
    <div class="product"><div class="product-photo" role="img" aria-label="Caramel cookies"></div><div class="product-name">Caramel Swirl</div><div class="product-price">$ 20.00</div></div>
    <div class="product"><div class="product-photo" role="img" aria-label="Chocolate chip cookies"></div><div class="product-name">Chocolate Chip 101</div><div class="product-price">$ 18.00</div></div>
    <div class="product"><div class="product-photo" role="img" aria-label="Iced almond cookies"></div><div class="product-name">Iced Almond</div><div class="product-price">$ 22.00</div></div>
    <div class="product"><div class="product-photo" role="img" aria-label="Iced lemon cookies"></div><div class="product-name">Iced Lemon</div><div class="product-price">$ 22.00</div></div>
    <div class="product"><div class="product-photo" role="img" aria-label="Iced sugar cookies"></div><div class="product-name">Iced Sugar Hearts</div><div class="product-price">$ 24.00</div></div>
    <div class="product"><div class="product-photo" role="img" aria-label="Peanut butter cookies"></div><div class="product-name">Peanut Butter Dipped</div><div class="product-price">$ 20.00</div></div>
    <div class="product"><div class="product-photo" role="img" aria-label="Vanilla cookies"></div><div class="product-name">Vanilla Dream</div><div class="product-price">$ 18.00</div></div>
    <div class="product"><div class="product-photo" role="img" aria-label="Pastry tarts"></div><div class="product-name">Pie Tarts</div><div class="product-price">$ 24.00</div></div>
  </div>
</section>

<footer class="site-footer">
  <div class="footer-col contact">
    <h4>CONTACT INFO</h4>
    <ul>
      <li><svg width="7" height="7" viewBox="0 0 10 10"><path d="M2 1l2 2-1 1.5c.7 1.3 1.5 2.1 2.5 2.5L7 6l2 2-1.5 1.5C4.5 9 1 5.5.5 2.5z" fill="#c8955a"/></svg>Phone: (555) 014-2280</li>
      <li><svg width="7" height="7" viewBox="0 0 10 10"><rect x=".5" y="2" width="9" height="6" fill="none" stroke="#c8955a"/><path d="M.5 2l4.5 3.5L9.5 2" fill="none" stroke="#c8955a"/></svg>Email: hello@tillysbiscuits.example</li>
      <li><svg width="7" height="7" viewBox="0 0 10 10"><circle cx="5" cy="5" r="4.3" fill="none" stroke="#c8955a"/><path d="M.7 5h8.6M5 .7c2.5 2.5 2.5 6.1 0 8.6M5 .7c-2.5 2.5-2.5 6.1 0 8.6" fill="none" stroke="#c8955a" stroke-width=".7"/></svg>Web: https://www.tillysbiscuits.example</li>
    </ul>
  </div>
  <div class="footer-col newsletter">
    <h4>SUBSCRIBE OUR NEWSLETTER</h4>
    <div class="subscribe"><span></span><b>SUBSCRIBE</b></div>
  </div>
  <div class="footer-col quick">
    <h4>QUICK LINKS</h4>
    <ul><li>HOME</li><li>ABOUT US</li><li>PRODUCTS</li><li>MENU</li><li>CONTACT US</li></ul>
  </div>
  <div class="footer-bar">
    <span>© Copyright 2018 Tilly's Biscuits. All rights reserved.</span>
    <span class="follow">Follow Us: <i></i><i></i><i></i><i></i><i></i><i></i></span>
  </div>
</footer>

</body>
</html>
```